Business card design for Marion Tate

I have a logo and will attach. The tag line is: Know your Numbers. The 'K' in Know could be red. There is a registered BAS Agent logo with my number to be incorporated onto the card and my photo (not sure about this though) as mixed reactions to photos on business cards.

I also have a training organisation called, Tallywise Training College and the red and black 'K" is in this name.

Target Market(s)

Medium to small businesses, tax agents, accountants,

Industry/Entity Type

Financial Service

Contact Information for Business Card

Logo with the name, BAS & Bookkeeping (Registered business name is "ZJ BAS & Bookkeeping").
My name: Marion Tate
Email: marion@tlwtc.com.au
M: 0412 863150
PO Box 7162 Ashwyn Qld 4127.
Web: www.tlwtc.com.au
Tag line "Know your numbers"

Font styles to use
Serif

Colors
ec1f27
000000

Requirements
Must have
• You can see from the logo 'ZJ" uploaded that it matches the ZJ in Bookkeeping, e.g. the second 'K' in Bookkeeping is to be red.
Nice to have
• I have had my photo before, but not so sure this time. Please advise. Landscape design. Clean and clear. White background.

```html
<!DOCTYPE html>
<html lang="en">
<head>
<meta charset="utf-8">
<title>Marion Tate – Business Card</title>
<link rel="stylesheet" href="https://fonts.googleapis.com/css2?family=Arimo:wght@400;700&family=Open+Sans:wght@400&display=swap">
<style>
  :root {
    --brand-red: #ec1f27;
    --ink: #000000;
    --paper: #ffffff;
    --divider: #d4d4d4;
    --backdrop: #3b3b3b;
    --photo-tone-a: #6f6a66;
    --photo-tone-b: #2a2626;
  }
  * { box-sizing: border-box; margin: 0; padding: 0; }
  html, body {
    width: 999px;
    height: 1200px;
    overflow: hidden;
    background: var(--backdrop);
  }
  .card {
    position: absolute;
    left: 199px;
    top: 74px;
    width: 601px;
    height: 1051px;
    background: var(--paper);
  }
  .card__header {
    position: absolute;
    left: 0; top: 0;
    width: 100%;
    height: 474px;
    background: var(--brand-red);
    border-bottom: 5px solid var(--ink);
  }
  .portrait {
    position: absolute;
    left: 150px;
    top: 60px;
    width: 300px;
    height: 300px;
    border-radius: 50%;
    border: 11px solid var(--paper);
    background: radial-gradient(circle at 50% 40%, var(--photo-tone-a), var(--photo-tone-b));
  }
  .holder-name {
    position: absolute;
    left: 0; top: 372px;
    width: 100%;
    text-align: center;
    font-family: "Arimo", Arial, sans-serif;
    font-weight: 700;
    font-size: 55px;
    color: var(--paper);
    letter-spacing: 0.2px;
  }
  .contact-row {
    position: absolute;
    left: 0;
    width: 100%;
    display: flex;
    align-items: center;
    padding-left: 33px;
    font-family: "Open Sans", Arial, sans-serif;
    color: var(--ink);
    border-bottom: 3px solid var(--divider);
  }
  .contact-row--email { top: 479px; height: 85px; font-size: 25px; }
  .contact-row--phone { top: 564px; height: 80px; font-size: 32px; }
  .contact-row__icon { width: 28px; height: 28px; margin-right: 15px; flex: none; }
  .postal-address {
    position: absolute;
    left: 33px;
    top: 659px;
    font-family: "Open Sans", Arial, sans-serif;
    font-size: 24px;
    color: var(--ink);
  }
  .brand-mark {
    position: absolute;
    left: 0; top: 752px;
    width: 100%;
    text-align: center;
    font-family: "Arimo", Arial, sans-serif;
    font-weight: 700;
    font-size: 112px;
    line-height: 1;
    color: var(--ink);
  }
  .tagline {
    position: absolute;
    left: 0; top: 884px;
    width: 100%;
    text-align: center;
    font-family: "Arimo", Arial, sans-serif;
    font-weight: 700;
    font-size: 35px;
    color: var(--ink);
  }
  .card__footer {
    position: absolute;
    left: 0; bottom: 0;
    width: 100%;
    height: 75px;
    background: var(--brand-red);
    border-top: 6px solid var(--ink);
    display: flex;
    align-items: center;
    justify-content: center;
    font-family: "Open Sans", Arial, sans-serif;
    font-size: 25px;
    letter-spacing: 3.5px;
    color: var(--paper);
  }
</style>
</head>
<body>
  <div class="card">
    <header class="card__header">
      <div class="portrait" role="img" aria-label="Portrait photograph of Marion Tate"></div>
      <h1 class="holder-name">Marion Tate</h1>
    </header>

    <div class="contact-row contact-row--email">
      <svg class="contact-row__icon" viewBox="0 0 28 28" aria-hidden="true">
        <path d="M2 11 L14 3 L26 11 V25 H2 Z" fill="var(--ink)"/>
        <path d="M5 12 L14 19 L23 12" fill="none" stroke="var(--paper)" stroke-width="2"/>
      </svg>
      <span>marion@tlwtc.com.au</span>
    </div>

    <div class="contact-row contact-row--phone">
      <svg class="contact-row__icon" viewBox="0 0 28 28" aria-hidden="true">
        <path d="M7 3 L11 8 L8.5 11 C10 15 13 18 17 19.5 L20 17 L25 21 L22 25 C12 25 3 16 3 6 Z" fill="var(--ink)"/>
        <path d="M16 4 A9 9 0 0 1 24 12 M16 8 A5 5 0 0 1 20 12" fill="none" stroke="var(--ink)" stroke-width="2"/>
      </svg>
      <span>0412 863150</span>
    </div>

    <p class="postal-address">PO Box 7162 Ashwyn Qld 4127.</p>

    <div class="brand-mark">ZJ</div>
    <p class="tagline">Know your numbers</p>

    <footer class="card__footer">www.tlwtc.com.au</footer>
  </div>
</body>
</html>
```